Visitenkartenerstellung für Dorvek-Estates
Zielgruppe
Männer und Frauen, junge Familien bis hin zum Senior.
Verkauf von hochwertigen Immobilien in Spanien.
Aufgabenstellung
Auf Grund unserer Namensänderung benötigen wir ein neues Visitenkartendesign.
Wir sind eine skandinavische Agentur für Luxus-Immobilien auf Mallorca.
Das Design sollte dementsprechend edel aber dennoch schlicht gestaltet sein!

```html
<!DOCTYPE html>
<html lang="en">
<head>
<meta charset="utf-8">
<title>Dorvek-Estates – Business Card</title>
<link rel="stylesheet" href="https://fonts.googleapis.com/css2?family=Arimo:wght@400;700&display=swap">
<style>
  :root {
    --brand-blue: #35659a;
    --band-blue: #8eaac8;
    --muted-grey: #8a8a8a;
    --ink: #111111;
    --card-edge: #5a5a5a;
    --paper: #ffffff;
  }
  * { margin: 0; padding: 0; box-sizing: border-box; }
  html, body {
    width: 976px;
    height: 1200px;
    overflow: hidden;
    background: var(--paper);
    font-family: "Arimo", Arial, sans-serif;
  }
  .sheet {
    position: relative;
    width: 976px;
    height: 1200px;
  }
  .card {
    position: absolute;
    left: 42px;
    width: 892px;
    background: var(--paper);
    border: 2px solid var(--card-edge);
    overflow: hidden;
  }
  .card--front { top: 37px; height: 528px; }
  .card--back { top: 626px; height: 523px; }
  .card__band {
    position: absolute;
    left: 0;
    right: 0;
    bottom: 0;
    height: 77px;
    background: var(--band-blue);
    border-top: 1px solid var(--card-edge);
  }
  .line {
    position: absolute;
    left: 0;
    right: 0;
    text-align: center;
    white-space: nowrap;
    line-height: 1;
  }
  .brand-name {
    top: 164px;
    font-size: 98px;
    font-weight: 400;
    color: var(--brand-blue);
    letter-spacing: 1px;
  }
  .brand-tagline {
    top: 281px;
    font-size: 36px;
    color: var(--muted-grey);
  }
  .person-name {
    top: 62px;
    font-size: 45px;
    font-weight: 700;
    color: var(--brand-blue);
  }
  .person-role {
    top: 118px;
    font-size: 26px;
    color: var(--muted-grey);
  }
  .contact {
    font-size: 33px;
    color: var(--ink);
  }
  .contact--address { top: 190px; }
  .contact--phone { top: 245px; }
  .contact--link { color: var(--brand-blue); }
  .contact--email { top: 294px; }
  .contact--web { top: 344px; }
</style>
</head>
<body>
  <main class="sheet">
    <section class="card card--front">
      <h1 class="line brand-name">Dorvek-Estates</h1>
      <p class="line brand-tagline">Luxury Real Estate Mallorca &amp; Ibiza</p>
      <div class="card__band"></div>
    </section>

    <section class="card card--back">
      <h2 class="line person-name">Karin Lindqvist</h2>
      <p class="line person-role">Property Manager</p>
      <p class="line contact contact--address">C. Mirador 4 - 07181 Portals Spain</p>
      <p class="line contact contact--phone">Tel. 971-555018 - Mobil +34 60055214</p>
      <p class="line contact contact--link contact--email">Lindqvist@dorvek-estates.com</p>
      <p class="line contact contact--link contact--web">www.dorvek-estates.se</p>
      <div class="card__band"></div>
    </section>
  </main>
</body>
</html>
```